Holiday Rental Leaflet

Want a DL size double sided leaflet to distribute via local businesses, markets, family and friends
HOLIDAY RENTALCarrickalinga - 17 Farrow Street Sleeps 8-10 (2 Queen, 1 Double, 2 bunks), 4 bedrooms, BIR to all bedrooms 2 Bathrooms, one with bath, 2 toilets Open Plan Lounge/Dining/Kitchen area Dining Table for 8 peopleReverse cycle airconditionerSlow combustion wood heaterTV/DVD, CD/RadioKitchen has m/wave, oven, fridge/freezer, dishwasherBBQ providedTimber decking with 2 outside tables and 12 chairs Washing Machine and dryer provided One street back from beach Smoke free zone No Pets
For further information or to book contact Joan on 0491 278 306 or email joanbirch62@veltranet.com.au

Requirements
Nice to have
• Have sent a variety of photos of the house. No need to use all of them, pick out the most relevant for the leaflet.

```html
<!DOCTYPE html>
<html lang="en">
<head>
<meta charset="utf-8">
<title>Carrickalinga Holiday Rental Leaflet</title>
<link href="https://fonts.googleapis.com/css2?family=Lato:wght@400;700&family=Lobster&display=swap" rel="stylesheet">
<style>
:root{
  --bg:#5b5b5b;
  --paper:#ffffff;
  --paper-edge:#f1f1f1;
  --ink:#3a3a3a;
  --red:#e0262b;
  --red-dark:#9e1418;
  --band:#2f2f2f;
  --band-light:#4a4a4a;
  --frame:#2b2b2b;
}
*{box-sizing:border-box;margin:0;padding:0}
html,body{width:1200px;height:900px;overflow:hidden}
body{background:var(--bg);position:relative;font-family:"Lato",Arial,sans-serif}
.leaflet{position:absolute;width:504px;height:710px;background:linear-gradient(180deg,var(--paper) 0%,var(--paper-edge) 100%);box-shadow:0 6px 18px rgba(0,0,0,.45);overflow:hidden}
.leaflet--front{left:66px;top:118px}
.leaflet--back{left:635px;top:116px}
.leaflet__topband{position:absolute;left:0;top:0;width:100%;height:14px;background:var(--band)}
.photo{position:absolute;border:2px solid var(--frame)}
.footer{position:absolute;left:0;bottom:0;width:100%;height:78px;background:linear-gradient(180deg,var(--band-light),var(--band));display:flex;align-items:center;justify-content:center;color:#fff}
.script{font-family:"Lobster",cursive}
.footer__cta{font-size:20px;white-space:nowrap}
.footer__phone{font-family:"Lato",sans-serif;font-size:27px;color:var(--red);margin:0 6px}
.footer__contacts{font-size:13px;justify-content:space-between;padding:0 18px;white-space:nowrap}
.footer__item{display:flex;align-items:center;gap:6px}
.footer__item svg{width:13px;height:13px;fill:var(--red);flex:none}
.badge{position:absolute;width:198px;height:98px;border-radius:50%;background:#fff;border:3px solid #cfcfcf;box-shadow:0 2px 6px rgba(0,0,0,.35);display:flex;flex-direction:column;align-items:center;justify-content:center}
.badge__town{font-family:"Lobster",cursive;font-size:25px;color:#2a2a2a;line-height:1.1;padding-bottom:4px;border-bottom:1px solid #bdbdbd}
.badge__street{font-size:16px;color:var(--red);margin-top:3px;white-space:nowrap}
.ribbon{position:absolute;width:200px;height:36px;background:linear-gradient(180deg,#ef3a3e,#c81a1f);color:#fff;font-family:"Lobster",cursive;font-size:22px;display:flex;align-items:center;justify-content:center;transform:rotate(-33deg);box-shadow:0 3px 5px rgba(0,0,0,.4)}
.ribbon__fold{position:absolute;width:0;height:0;border-top:10px solid var(--red-dark);border-left:10px solid transparent}
.details{position:absolute;left:20px;top:214px;width:285px;color:var(--ink)}
.details__title{font-family:"Lobster",cursive;color:var(--red);font-size:21px;margin-bottom:6px}
.features{list-style:none;font-size:12.5px;line-height:15px}
.features li{position:relative;padding-left:16px;margin-bottom:7.4px}
.features li::before{content:"";position:absolute;left:0;top:5px;width:6px;height:6px;border-radius:50%;background:var(--red)}
</style>
</head>
<body>

<section class="leaflet leaflet--front">
  <div class="leaflet__topband"></div>
  <div class="photo" style="left:18px;top:24px;width:468px;height:180px;background:linear-gradient(180deg,#dfe8ee 0%,#8a9ea0 45%,#5d6b55 100%)" role="img" aria-label="Photo of the raised timber holiday house with front stairs"></div>
  <div class="photo" style="left:18px;top:214px;width:310px;height:208px;background:linear-gradient(180deg,#9fc6e6 0%,#2f6fb5 35%,#1e5596 55%,#4f7d3d 80%,#3b5f2a 100%)" role="img" aria-label="Photo of the ocean view over coastal shrubs"></div>
  <div class="photo" style="left:337px;top:214px;width:149px;height:208px;background:linear-gradient(160deg,#a3a3a3,#6a6a6a)" role="img" aria-label="Greyscale photo of a palm garden"></div>
  <div class="photo" style="left:18px;top:430px;width:468px;height:192px;background:linear-gradient(180deg,#d6e2d6 0%,#3fb19a 30%,#7e8e86 60%,#9a7a55 100%)" role="img" aria-label="Photo of the timber deck with green umbrellas and outdoor tables"></div>
  <div class="badge" style="left:236px;top:158px">
    <div class="badge__town">Carrickalinga</div>
    <div class="badge__street">17 Farrow Street</div>
  </div>
  <div class="ribbon__fold" style="left:14px;top:556px"></div>
  <div class="ribbon" style="left:-6px;top:470px">Book Now</div>
  <div class="footer footer__cta script">
    <span>Contact Joan at</span><span class="footer__phone">0491 278 306</span><span>and Book Now</span>
  </div>
</section>

<section class="leaflet leaflet--back">
  <div class="leaflet__topband"></div>
  <div class="photo" style="left:17px;top:26px;width:468px;height:178px;background:linear-gradient(180deg,#dfe8ee 0%,#8a9ea0 45%,#5d6b55 100%)" role="img" aria-label="Photo of the raised timber holiday house with front stairs"></div>
  <div class="ribbon__fold" style="left:13px;top:128px"></div>
  <div class="ribbon" style="left:-10px;top:46px">Book Now</div>
  <div class="photo" style="left:323px;top:209px;width:162px;height:200px;background:linear-gradient(180deg,#c7b59c 0%,#8c7a66 50%,#a45b3e 100%)" role="img" aria-label="Photo of the slow combustion wood heater on a stone hearth"></div>
  <div class="photo" style="left:323px;top:416px;width:162px;height:214px;background:linear-gradient(180deg,#d99a4f 0%,#c07a35 55%,#9a5a22 100%)" role="img" aria-label="Photo of the timber dining area with table and chairs"></div>
  <div class="badge" style="left:290px;top:134px">
    <div class="badge__town">Carrickalinga</div>
    <div class="badge__street">17 Farrow Street</div>
  </div>
  <div class="details">
    <h2 class="details__title">Carrickalinga</h2>
    <ul class="features">
      <li>Sleeps 8-10</li>
      <li>(2 Queen, 1 Double, 2 bunks), 4 bedrooms,</li>
      <li>BIR to all bedrooms</li>
      <li>2 Bathrooms, one with bath, 2 toilets</li>
      <li>Open Plan Lounge/Dining/Kitchen area</li>
      <li>Dining Table for 8 people</li>
      <li>Reverse cycle airconditioner</li>
      <li>Slow combustion wood heater</li>
      <li>TV/DVD, CD/Radio</li>
      <li>Kitchen has m/wave, oven, fridge/freezer, dishwasher</li>
      <li>BBQ provided</li>
      <li>Timber decking with 2 outside tables and 12 chairs</li>
      <li>Washing Machine and dryer provided</li>
      <li>One street back from beach</li>
      <li>Smoke free zone</li>
      <li>No Pets</li>
    </ul>
  </div>
  <div class="footer footer__contacts">
    <span class="footer__item"><svg viewBox="0 0 24 24"><path d="M6.6 10.8a15 15 0 0 0 6.6 6.6l2.2-2.2a1 1 0 0 1 1-.25 11.4 11.4 0 0 0 3.6.57 1 1 0 0 1 1 1V20a1 1 0 0 1-1 1A17 17 0 0 1 3 4a1 1 0 0 1 1-1h3.5a1 1 0 0 1 1 1c0 1.25.2 2.45.57 3.57a1 1 0 0 1-.25 1z"/></svg>0491 278 306</span>
    <span class="footer__item"><svg viewBox="0 0 24 24"><path d="M12 3 2 12h3v8h5v-6h4v6h5v-8h3z"/></svg>17 Farrow Street</span>
    <span class="footer__item"><svg viewBox="0 0 24 24"><path d="M2 5h20v14H2z"/><path d="M2 5l10 8 10-8" stroke="#2f2f2f" stroke-width="1.8" fill="none"/></svg>joanbirch62@veltranet.com.au</span>
  </div>
</section>

</body>
</html>
```